Criação de Cartao de Visita para Vigor & Equilíbrio
" Venda de Suplementos Alimentares/Nutricionais, principalmente via whatsapp e facebook, fazemos entregas e aceitamos cartões. Ainda não possuimos loja física. Cobrimos qualquer oferta de site ou loja nacional. "

```html
<!DOCTYPE html>
<html lang="pt-BR">
<head>
<meta charset="UTF-8">
<title>Vigor &amp; Equilíbrio — Cartão de Visita</title>
<link href="https://fonts.googleapis.com/css2?family=Montserrat:wght@800&family=Arimo:wght@400;700&display=swap" rel="stylesheet">
<style>
  :root {
    --page: #ecebe8;
    --card-black: #0b0b0b;
    --card-white: #ffffff;
    --gold: #f7b21b;
    --orange: #f08a12;
    --text-light: #e9e9e9;
    --text-dark: #2a2a2a;
    --text-muted: #555555;
  }
  * { margin: 0; padding: 0; box-sizing: border-box; }
  html, body {
    width: 1200px; height: 1200px; overflow: hidden;
    background: var(--page);
    font-family: "Arimo", Arial, sans-serif;
  }
  .sheet {
    width: 1200px; height: 1200px;
    display: flex; flex-direction: column; align-items: center; justify-content: center;
    gap: 60px;
  }
  .card {
    width: 900px; height: 500px;
    border-radius: 26px;
    overflow: hidden;
    position: relative;
    background: var(--card-black);
  }

  /* Front */
  .card-front__header {
    height: 190px; background: var(--card-white);
    position: relative;
    display: flex; align-items: center;
    padding: 0 70px;
  }
  .card-front__header::after {
    content: ""; position: absolute; left: 50%; bottom: 0;
    transform: translateX(-50%);
    border-left: 12px solid transparent; border-right: 12px solid transparent;
    border-bottom: 12px solid var(--orange);
  }
  .brand {
    display: flex; align-items: center; gap: 14px;
    font-family: "Montserrat", sans-serif; font-weight: 800;
    color: var(--gold); text-transform: uppercase; letter-spacing: 0.5px;
  }
  .brand__dot { border-radius: 50%; background: var(--gold); flex: none; }
  .brand--small { font-size: 26px; width: 380px; }
  .brand--small .brand__dot { width: 22px; height: 22px; }
  .person { margin-left: 60px; }
  .person__name {
    font-size: 24px; letter-spacing: 3px; color: var(--text-dark); text-transform: uppercase;
  }
  .person__role {
    margin-top: 8px; font-size: 14px; letter-spacing: 2px; color: var(--text-muted); text-transform: uppercase;
  }
  .contacts {
    display: flex; gap: 70px; padding: 44px 40px 0 40px;
  }
  .contacts__col { display: flex; flex-direction: column; gap: 16px; }
  .contacts__col--left { width: 430px; }
  .contact {
    display: flex; align-items: center; gap: 16px;
    color: var(--text-light); font-size: 22px;
  }
  .contact__icon {
    width: 24px; height: 24px; border-radius: 4px; background: var(--orange);
    display: flex; align-items: center; justify-content: center; flex: none;
  }

  /* Back */
  .card-back {
    display: flex; align-items: center; justify-content: center;
  }
  .card-back::after {
    content: ""; position: absolute; left: 0; right: 0; bottom: 0; height: 16px;
    background: linear-gradient(90deg, var(--orange), var(--gold), var(--orange));
  }
  .brand--large { font-size: 46px; flex-direction: column; gap: 26px; }
  .brand--large .brand__dot { width: 110px; height: 110px; }
</style>
</head>
<body>
<main class="sheet">

  <section class="card card-front" aria-label="Frente do cartão">
    <header class="card-front__header">
      <div class="brand brand--small"><span class="brand__dot"></span><span>Vigor &amp; Equilíbrio</span></div>
      <div class="person">
        <p class="person__name">Nome Sobrenome</p>
        <p class="person__role">Função</p>
      </div>
    </header>
    <div class="contacts">
      <ul class="contacts__col contacts__col--left" style="list-style:none">
        <li class="contact">
          <span class="contact__icon"><svg width="14" height="14" viewBox="0 0 14 14"><path d="M7 1a4 4 0 0 0-4 4c0 3 4 8 4 8s4-5 4-8a4 4 0 0 0-4-4zm0 5.5A1.5 1.5 0 1 1 7 3.5a1.5 1.5 0 0 1 0 3z" fill="#111"/></svg></span>
          Rua do Projeto, 000, Cidade/Estado
        </li>
        <li class="contact">
          <span class="contact__icon"><svg width="14" height="14" viewBox="0 0 14 14"><path d="M3 1.5l2 .3 1 2.7-1.3 1a7 7 0 0 0 3.8 3.8l1-1.3 2.7 1 .3 2A1.5 1.5 0 0 1 11 12.5 9.5 9.5 0 0 1 1.5 3 1.5 1.5 0 0 1 3 1.5z" fill="#111"/></svg></span>
          (00) 0000-0000
        </li>
        <li class="contact">
          <span class="contact__icon"><svg width="14" height="14" viewBox="0 0 14 14"><path d="M3 1.5l2 .3 1 2.7-1.3 1a7 7 0 0 0 3.8 3.8l1-1.3 2.7 1 .3 2A1.5 1.5 0 0 1 11 12.5 9.5 9.5 0 0 1 1.5 3 1.5 1.5 0 0 1 3 1.5z" fill="#111"/></svg></span>
          (00) 0000-0000
        </li>
      </ul>
      <ul class="contacts__col" style="list-style:none">
        <li class="contact">
          <span class="contact__icon"><svg width="14" height="14" viewBox="0 0 14 14"><rect x="1.5" y="3" width="11" height="8" rx="1" fill="#111"/><path d="M1.5 3.5L7 7.5l5.5-4" stroke="#f08a12" stroke-width="1.2" fill="none"/></svg></span>
          contato@vigorequilibrio.com.br
        </li>
        <li class="contact">
          <span class="contact__icon"><svg width="14" height="14" viewBox="0 0 14 14"><circle cx="7" cy="7" r="5.5" fill="none" stroke="#111" stroke-width="1.4"/><path d="M1.5 7h11M7 1.5c-2.5 3-2.5 8 0 11M7 1.5c2.5 3 2.5 8 0 11" stroke="#111" stroke-width="1.1" fill="none"/></svg></span>
          www.vigorequilibrio.com.br
        </li>
      </ul>
    </div>
  </section>

  <section class="card card-back" aria-label="Verso do cartão">
    <div class="brand brand--large"><span class="brand__dot"></span><span>Vigor &amp; Equilíbrio</span></div>
  </section>

</main>
</body>
</html>
```